Maple Hollow Cedar Bend Restaurant Week

We need our flyer from last year updated. Please use this year's logo, attached below and use a similar overall layout as last year's flyer, which is also attached. The goal is to make this year's flyer less cluttered.

1. Remove the cornucopia/food background, and instead incorporate an attractive table, wine glass(es) and possibly a wine bottle.

2. Include this year's logo, attached, prominently in the middle of the flyer, possibly larger.

3. Take out the prices and the 4 buttons/circles with the price options all together.

4. Include the logos for Lantern Festival and the Maple Hollow Urban District (with the fountain), attached.

The website should be changed to: MHCBRestaurantWeek.com

```html
<!DOCTYPE html>
<html lang="en">
<head>
<meta charset="utf-8">
<title>Maple Hollow Cedar Bend Restaurant Week flyer</title>
<link rel="stylesheet" href="https://fonts.googleapis.com/css2?family=Merriweather:wght@400;700;900&display=swap">
<style>
  :root {
    --page-bg: #e9e9e7;
    --wood-light: #7a5434;
    --wood-mid: #5e3e24;
    --wood-dark: #3b2616;
    --photo-warm: #b8793a;
    --photo-deep: #5a3418;
    --logo-red: #e8484a;
    --band-red: #ee4a4c;
    --footer-dark: #2c221b;
    --text-light: #ffffff;
    --text-soft: #efe4d8;
    --partner-teal: #2aa3a8;
  }
  * { margin: 0; padding: 0; box-sizing: border-box; }
  html, body {
    width: 1200px; height: 1000px; overflow: hidden;
    background: var(--page-bg);
    font-family: "Merriweather", Georgia, serif;
  }
  .flyer {
    position: absolute; left: 320px; top: 38px;
    width: 560px; height: 924px; overflow: hidden;
    background: linear-gradient(180deg, var(--wood-light) 0%, var(--wood-mid) 55%, var(--wood-dark) 100%);
    box-shadow: 0 6px 18px rgba(0,0,0,.25);
  }
  .hero-photo {
    position: absolute; left: 0; top: 0; width: 560px; height: 300px;
    background:
      radial-gradient(ellipse at 55% 35%, #d89a52 0%, transparent 60%),
      linear-gradient(180deg, var(--photo-warm) 0%, var(--photo-deep) 100%);
  }
  .hero-photo::after {
    content: ""; position: absolute; left: 0; right: 0; bottom: 0; height: 90px;
    background: linear-gradient(180deg, transparent, var(--wood-light));
  }
  .event-mark {
    position: absolute; left: 42px; top: 152px;
    width: 476px; height: 476px; border-radius: 50%;
    background: var(--logo-red);
    box-shadow: 0 8px 20px rgba(0,0,0,.35);
    display: flex; align-items: center; justify-content: center;
    text-align: center;
  }
  .event-name {
    color: var(--text-light); font-weight: 900;
    font-size: 40px; line-height: 1.15; text-transform: uppercase;
    letter-spacing: 1px; width: 340px;
  }
  .event-dates {
    position: absolute; left: 0; width: 100%; top: 640px;
    text-align: center; color: var(--text-light);
    font-weight: 700; font-size: 19px;
  }
  .host {
    position: absolute; left: 0; width: 100%; top: 676px;
    text-align: center; color: var(--text-soft);
  }
  .host-label { font-size: 12px; font-weight: 400; }
  .host-office { font-size: 16px; font-weight: 700; color: var(--text-light); margin-top: 8px; }
  .host-name { font-size: 26px; font-weight: 900; color: var(--text-light); margin-top: 4px; }
  .partners {
    position: absolute; left: 0; width: 100%; top: 770px;
    display: flex; justify-content: center; align-items: center; gap: 22px;
  }
  .partner {
    display: flex; align-items: center; gap: 8px;
    color: var(--partner-teal); font-size: 11px; font-weight: 700;
    text-transform: uppercase; line-height: 1.25; width: 150px;
  }
  .partner:first-child { justify-content: flex-end; text-align: right; }
  .partner-dot { width: 22px; height: 22px; border-radius: 50%; background: var(--partner-teal); flex: none; }
  .partner-divider { width: 1px; height: 46px; background: var(--text-soft); opacity: .8; }
  .web-band {
    position: absolute; left: 0; top: 836px; width: 560px; height: 34px;
    background: var(--band-red);
    color: var(--text-light); font-weight: 900; font-size: 22px;
    text-align: center; line-height: 34px;
  }
  .social-bar {
    position: absolute; left: 0; top: 870px; width: 560px; height: 54px;
    background: var(--footer-dark);
    display: flex; justify-content: space-around; align-items: center;
    padding: 0 18px;
  }
  .social-item {
    display: flex; align-items: center; gap: 6px;
    color: var(--text-soft); font-size: 8.5px; font-weight: 400;
  }
  .social-square { width: 20px; height: 20px; background: #6c7a91; flex: none; }
</style>
</head>
<body>
  <main class="flyer">
    <div class="hero-photo" role="img" aria-label="Photo of a wooden table with wine bottles, a wine glass, a basket of grapes and a trumpet"></div>

    <div class="event-mark">
      <div class="event-name">Maple Hollow Cedar Bend Restaurant Week</div>
    </div>
    <div class="event-dates">September 6 - 11, 2016</div>

    <section class="host">
      <div class="host-label">Hosted by:</div>
      <div class="host-office">Ashford County Councilmember</div>
      <div class="host-name">Dana Whitlock</div>
    </section>

    <section class="partners">
      <div class="partner"><span>Maple Hollow<br>Lantern Festival</span><span class="partner-dot"></span></div>
      <div class="partner-divider"></div>
      <div class="partner"><span class="partner-dot"></span><span>Maple Hollow<br>Urban District</span></div>
    </section>

    <div class="web-band">www.MHCBRestaurantWeek.com</div>

    <footer class="social-bar">
      <div class="social-item"><span class="social-square"></span>Maplehollowrestaurantweek</div>
      <div class="social-item"><span class="social-square"></span>@MapleHollowRW #MHRW</div>
      <div class="social-item"><span class="social-square"></span>@maplehollowrestaurantweek</div>
    </footer>
  </main>
</body>
</html>
```